Upbeat Accouting Package Flyer

I am looking for a 1 page (front, or front and back) flyer that will become our marketing for our accounting services. We are looking for something a little different and we are catering to the small retail shop owners. We have 3 accounting packages we would like to display and then some add-ons. I have included our logo that must be included in the design. I have uploaded the accounting package information as well.
Target Market(s)
Small Retail Shop Owners
Industry/Entity Type
Accounting
Colors
Designer to choose colors to be used in the design.
Requirements
Must have
- A casual feel. We are not your typical accountants who are very professional and "stuffy". I want it to feel like we are all family.
Nice to have
- I would like to incorporate some sort of retail theme.
- We have a couple of taglines we like to use and it would be great if they could be included. They are "We know you CAN do the accounting, but do you WANT to?" and "We allow you to get back to what's important."
Should not have
- Typical stock accounting photos of people shaking hands, large office buildings, etc.

```html
<!DOCTYPE html>
<html lang="en">
<head>
<meta charset="utf-8">
<title>Larkfield Tax and Accounting – Accounting Packages Flyer</title>
<link href="https://fonts.googleapis.com/css2?family=Arimo:wght@400;700&family=Caveat+Brush&display=swap" rel="stylesheet">
<style>
  :root {
    --page: #ffffff;
    --flyer: #000000;
    --ink: #ffffff;
    --rule: #8a8a8a;
    --develop: #4a8fcb;
    --grow: #5fc46b;
    --relax: #f7b865;
    --options: #f27679;
    --accent: #1fb3d6;
  }
  * { box-sizing: border-box; margin: 0; padding: 0; }
  html, body { width: 1200px; height: 1000px; overflow: hidden; background: var(--page); }
  body { position: relative; font-family: "Arimo", Arial, sans-serif; color: var(--ink); }

  .flyer { position: absolute; left: 302px; top: 62px; width: 596px; height: 841px; background: var(--flyer); }

  .photo { position: absolute; top: 13px; height: 320px; }
  .photo--jackets { left: 20px; width: 176px; background: linear-gradient(100deg, #c91d1a 0%, #e0323a 35%, #b01fb0 60%, #2d6e63 100%); }
  .photo--market  { left: 209px; width: 178px; background: linear-gradient(170deg, #234a9a 0%, #3a3f78 30%, #b8643a 60%, #d9924f 100%); }
  .photo--shelves { left: 398px; width: 178px; background: linear-gradient(180deg, #e8a21d 0%, #f0a92a 40%, #d9482f 70%, #e89a1a 100%); }

  .tagline {
    position: absolute; left: 0; top: 352px; width: 596px; text-align: center;
    font-family: "Caveat Brush", cursive; font-size: 37px; line-height: 38px;
  }

  .section-title { position: absolute; left: 20px; top: 448px; width: 558px; display: flex; align-items: center; gap: 16px; }
  .section-title::before, .section-title::after { content: ""; flex: 1; height: 1px; background: var(--rule); }
  .section-title h2 { font-weight: 400; font-size: 19px; }

  .package { position: absolute; top: 485px; width: 186px; }
  .package--develop { left: 14px; }
  .package--grow { left: 205px; }
  .package--relax { left: 395px; }
  .package__tab { height: 35px; border-radius: 0 14px 0 0; font-size: 16px; display: flex; align-items: center; justify-content: center; }
  .package--develop .package__tab { background: var(--develop); }
  .package--grow .package__tab { background: var(--grow); }
  .package--relax .package__tab { background: var(--relax); }
  .package__body { padding: 10px 8px 0 16px; font-size: 9.4px; line-height: 12px; }
  .package__body ul { list-style: none; }
  .package__body li { padding-left: 8px; text-indent: -8px; }
  .package__body li::before { content: "• "; }
  .package--grow .package__body, .package--relax .package__body { border-left: 1px solid var(--rule); margin-top: 8px; padding-top: 2px; height: 200px; }

  .options {
    position: absolute; left: 14px; top: 749px; width: 306px; height: 82px;
    background: var(--options); border-radius: 12px; padding: 10px 16px; font-size: 9.4px; line-height: 12px;
  }
  .options strong { display: block; }

  .brand { position: absolute; left: 348px; top: 762px; width: 220px; }
  .brand__name { font-size: 40px; font-weight: 700; line-height: 40px; display: flex; align-items: center; gap: 8px; }
  .brand__name::before { content: ""; width: 12px; height: 12px; border-radius: 50%; background: var(--accent); }
  .brand__sub { font-size: 8.6px; font-weight: 700; letter-spacing: 0.4px; margin-left: 68px; }
</style>
</head>
<body>
  <main class="flyer">
    <div class="photo photo--jackets" role="img" aria-label="Photo of colourful puffer jackets on a retail rack"></div>
    <div class="photo photo--market" role="img" aria-label="Photo of a market vendor behind stacked jars of preserves"></div>
    <div class="photo photo--shelves" role="img" aria-label="Photo of colourful notebooks on shop shelves"></div>

    <p class="tagline">We know you CAN do the<br>accounting, but do you WANT to?</p>

    <div class="section-title"><h2>Accounting Packages</h2></div>

    <section class="package package--develop">
      <div class="package__tab">Develop</div>
      <div class="package__body">
        <strong>$300/mo</strong> when paid annually<br>
        <strong>$325/mo</strong> billed monthly
        <ul>
          <li>LedgerCloud Online subscription</li>
          <li>Free accounting setup</li>
          <li>Weekly transaction processing</li>
          <li>Monthly account reconciliation (up to 2 accounts)</li>
          <li>Monthly financial statements by the 15th of the month</li>
        </ul>
      </div>
    </section>

    <section class="package package--grow">
      <div class="package__tab">Grow</div>
      <div class="package__body">
        <strong>$550/mo</strong> billed annually;<br>
        <strong>$575/mo</strong> billed monthly
        <ul>
          <li>LedgerCloud Online subscription</li>
          <li>Free accounting setup</li>
          <li>Weekly transaction processing</li>
          <li>Monthly account reconciliation (up to 4 accounts)</li>
          <li>Monthly financial statements by the 10th of the month</li>
          <li>Client portal access for document sharing</li>
          <li>1 Custom Report</li>
          <li>Accounts Payable</li>
          <li>Monthly Scorecard (customized metric tracking for your business)</li>
        </ul>
      </div>
    </section>

    <section class="package package--relax">
      <div class="package__tab">Relax (We've Got This)</div>
      <div class="package__body">
        <strong>$850/mo</strong> billed annually;<br>
        <strong>$875/mo</strong> billed monthly
        <ul>
          <li>LedgerCloud Online subscription</li>
          <li>Free accounting setup</li>
          <li>Weekly transaction processing</li>
          <li>Monthly account reconciliation (up to 5-10 accounts)</li>
          <li>Monthly financial statements by the 5th of the month</li>
          <li>Client portal access for document sharing</li>
          <li>2 Custom Reports</li>
          <li>Accounts Payable</li>
          <li>Invoicing and accounts receivable</li>
          <li>Weekly Scorecard (customized metric tracking for your business)</li>
        </ul>
      </div>
    </section>

    <aside class="options">
      <strong>Additional Options</strong>
      Payroll – 1-10 employees $85/mo; 11-30 employees $175/mo<br>
      Sales tax - $30/mo per state<br>
      Corporate taxes $50/mo<br>
      Owner taxes - $25/mo
    </aside>

    <div class="brand">
      <div class="brand__name">larkfield</div>
      <div class="brand__sub">TAX AND ACCOUNTING INC.</div>
    </div>
  </main>
</body>
</html>
```